Dr. Plume Southern Reef Oil

We need a bottle label design for a new company called Dr. Plume. We sell krill oil in gel caps. Krill are shrimp-like crustaceans. We are looking for a professional concept that communicates the essence of ocean, health, life, purity...maybe a krill with medical authority.

There are a few labels out there. I attached 2. Dr. Halvorsen has some nice vector krill art, though the label is otherwise sparse. Copper Meadow has the feel of a nice full line of professional products, though there's nothing particularly krilly about it. Could there be a happy marriage of the two?

What we do NOT want is a photograph of an ocean with words over it. That screams Japanese karaoke.

Auxiliary wording on label front:
Heart Health
Southern Reef
100% Pure
Dietary Supplements
1000mg

I apologize to designers for my new-to-crowd-design vagueness above, but I will try to be very forthcoming with feedback.

Thank you all!

Target Market(s)

Krill oil buyers. The 40+ crowd who want their Omega 3s and know that krill oil has it in spades!

Requirements
Nice to have
• A singular image that can be lifted for website branding as well...

```html
<!DOCTYPE html>
<html lang="en">
<head>
<meta charset="utf-8">
<title>Dr. Plume Southern Reef Oil – Label Designs</title>
<link href="https://fonts.googleapis.com/css2?family=Arimo:wght@400;700&family=Libre+Baskerville:wght@700&display=swap" rel="stylesheet">
<style>
  :root {
    --bg-top: #e9ebeb;
    --bg-bottom: #f7f8f8;
    --navy: #1f4f8f;
    --teal-deep: #1d4f5c;
    --teal-mid: #2b6373;
    --wave-light: #cfe0ec;
    --wave-mid: #8fb3cf;
    --wave-blue: #4a86b4;
    --gold-text: #e2b23c;
    --gold-light: #f6dc8a;
    --gold-mid: #d9a93a;
    --gold-dark: #b98420;
    --white: #ffffff;
    --krill-coral: #ec7a5a;
    --map-blue: #3f8fc6;
  }
  * { box-sizing: border-box; margin: 0; padding: 0; }
  html, body {
    width: 1200px; height: 825px; overflow: hidden;
    background: linear-gradient(180deg, var(--bg-top), var(--bg-bottom));
    font-family: "Arimo", Arial, sans-serif;
  }
  .label-row {
    width: 1200px; height: 825px;
    display: flex; justify-content: center; align-items: center; gap: 80px;
  }
  .label {
    position: relative;
    width: 420px; height: 470px;
    overflow: hidden;
    box-shadow: 0 6px 22px rgba(0,0,0,0.18);
  }
  .label--classic { background: var(--white); }
  .label--gold {
    background: linear-gradient(90deg, var(--gold-dark), var(--gold-light) 45%, var(--gold-mid) 75%, var(--gold-dark));
  }
  .label__waves { position: absolute; left: 0; top: 0; width: 420px; height: 470px; }
  .brand {
    position: absolute; left: 0; right: 0; top: 34px;
    display: flex; justify-content: center; align-items: center; gap: 8px;
  }
  .brand__mark { width: 12px; height: 12px; background: var(--navy); }
  .brand__name {
    font-family: "Arimo", Arial, sans-serif; font-weight: 700;
    font-size: 24px; color: var(--navy);
  }
  .range-name {
    position: absolute; left: 0; right: 0; top: 78px;
    text-align: center; font-weight: 700; font-size: 20px;
    letter-spacing: 4px; color: var(--navy);
  }
  .label--gold .range-name { letter-spacing: 3px; }
  .hero-art {
    position: absolute; left: 140px; top: 118px;
    width: 170px; height: 150px; border-radius: 46% 54% 50% 50%;
    background: radial-gradient(circle at 42% 50%, var(--krill-coral) 0 34%, var(--map-blue) 36% 100%);
  }
  .heart-badge {
    position: absolute; left: 22px; top: 172px;
    display: flex; align-items: center; gap: 6px;
    color: var(--navy); font-weight: 700; font-size: 17px; line-height: 1.05;
  }
  .heart-badge svg { width: 26px; height: 24px; }
  .claims {
    position: absolute; left: 0; right: 0; top: 318px;
    text-align: center; color: var(--white);
  }
  .claims__purity { font-weight: 700; font-size: 17px; letter-spacing: 0.5px; }
  .claims__product {
    font-family: "Libre Baskerville", Georgia, serif; font-weight: 700;
    font-size: 38px; color: var(--gold-text); margin-top: 2px; line-height: 1.15;
  }
  .claims__dose { font-size: 18px; margin-top: 2px; }
  .claims__footer {
    display: flex; justify-content: space-between;
    padding: 0 26px; margin-top: 10px;
    font-weight: 700; font-size: 16px; color: var(--gold-text);
  }
</style>
</head>
<body>
<main class="label-row">

  <section class="label label--classic">
    <svg class="label__waves" viewBox="0 0 420 470" aria-hidden="true">
      <path d="M0 250 C120 200 260 215 420 180 L420 230 C280 250 140 240 0 290 Z" fill="var(--wave-light)"/>
      <path d="M0 275 C130 235 270 245 420 215 L420 245 C270 270 140 265 0 305 Z" fill="var(--wave-mid)"/>
      <path d="M0 300 C140 265 280 270 420 240 L420 470 L0 470 Z" fill="var(--teal-deep)"/>
      <path d="M0 300 C140 265 280 270 420 240 L420 255 C280 285 140 282 0 318 Z" fill="var(--teal-mid)"/>
    </svg>
    <div class="brand"><span class="brand__mark"></span><span class="brand__name">Dr. Plume's</span></div>
    <div class="range-name">SOUTHERN REEF</div>
    <div class="hero-art" role="img" aria-label="Illustration of a coral-coloured krill over a blue map of the southern polar continent"></div>
    <div class="heart-badge">
      <svg viewBox="0 0 26 24"><path d="M13 22 C4 15 1 11 1 7 A5.5 5.5 0 0 1 13 5 A5.5 5.5 0 0 1 25 7 C25 11 22 15 13 22 Z" fill="none" stroke="var(--navy)" stroke-width="2"/></svg>
      <span>Heart<br>Health</span>
    </div>
    <div class="claims">
      <p class="claims__purity">100% PURE</p>
      <p class="claims__product">Krill Oil</p>
      <p class="claims__dose">1000mg</p>
      <p class="claims__footer"><span>60 Softgels</span><span>Dietary Supplement</span></p>
    </div>
  </section>

  <section class="label label--gold">
    <svg class="label__waves" viewBox="0 0 420 470" aria-hidden="true">
      <path d="M0 250 C120 200 260 215 420 180 L420 230 C280 250 140 240 0 290 Z" fill="var(--wave-mid)"/>
      <path d="M0 275 C130 235 270 245 420 215 L420 245 C270 270 140 265 0 305 Z" fill="var(--wave-blue)"/>
      <path d="M0 300 C140 265 280 270 420 240 L420 470 L0 470 Z" fill="var(--teal-deep)"/>
      <path d="M0 300 C140 265 280 270 420 240 L420 255 C280 285 140 282 0 318 Z" fill="var(--gold-mid)"/>
    </svg>
    <div class="brand"><span class="brand__mark"></span><span class="brand__name">Dr. Plume's</span></div>
    <div class="range-name">SOUTHERN REEF GOLD</div>
    <div class="hero-art" role="img" aria-label="Illustration of a coral-coloured krill over a blue map of the southern polar continent"></div>
    <div class="heart-badge">
      <svg viewBox="0 0 26 24"><path d="M13 22 C4 15 1 11 1 7 A5.5 5.5 0 0 1 13 5 A5.5 5.5 0 0 1 25 7 C25 11 22 15 13 22 Z" fill="var(--white)" stroke="var(--navy)" stroke-width="2"/></svg>
      <span>Heart<br>Health</span>
    </div>
    <div class="claims">
      <p class="claims__purity">100% PURE</p>
      <p class="claims__product">Krill Oil</p>
      <p class="claims__dose">1000mg</p>
      <p class="claims__footer"><span>60 Softgels</span><span>Dietary Supplement</span></p>
    </div>
  </section>

</main>
</body>
</html>
```